Business Cards

Business card design for my company.
I would like the card's background colour to be black. You can also see our web site to get an idea of our brand. https://www.dlqmarrowfield.com.au/
- Name
- Email

```html
<!DOCTYPE html>
<html lang="en">
<head>
<meta charset="utf-8">
<title>DLQ Marrowfield – Business Card</title>
<link href="https://fonts.googleapis.com/css2?family=Montserrat:wght@400;700&display=swap" rel="stylesheet">
<style>
  :root {
    --page: #e4e4e4;
    --card: #000000;
    --ink: #ffffff;
    --accent: #1f9a4a;
  }
  * { margin: 0; padding: 0; box-sizing: border-box; }
  html, body {
    width: 1200px;
    height: 1200px;
    overflow: hidden;
    background: var(--page);
    font-family: "Montserrat", sans-serif;
  }
  .card {
    position: absolute;
    left: 170px;
    width: 860px;
    height: 502px;
    background: var(--card);
    color: var(--ink);
  }
  .card--front { top: 82px; }
  .card--back { top: 616px; }

  .wordmark {
    position: absolute;
    display: flex;
    align-items: center;
    gap: 14px;
    font-weight: 700;
    color: var(--ink);
    letter-spacing: 0.06em;
    white-space: nowrap;
  }
  .wordmark__square {
    background: var(--accent);
    flex: none;
  }
  .card--front .wordmark {
    right: 70px;
    top: 128px;
    font-size: 30px;
  }
  .card--front .wordmark__square { width: 22px; height: 22px; }
  .card--back .wordmark {
    left: 50%;
    top: 50%;
    transform: translate(-50%, -50%);
    font-size: 46px;
  }
  .card--back .wordmark__square { width: 32px; height: 32px; }

  .holder {
    position: absolute;
    left: 64px;
    top: 262px;
    display: flex;
    align-items: center;
    gap: 26px;
  }
  .holder__name {
    font-weight: 700;
    font-size: 28px;
    letter-spacing: 0.02em;
    text-transform: uppercase;
  }
  .holder__rule {
    width: 112px;
    height: 4px;
    background: var(--accent);
    margin-top: 6px;
  }

  .contacts {
    position: absolute;
    left: 64px;
    top: 337px;
    list-style: none;
  }
  .contacts__item {
    display: flex;
    align-items: center;
    height: 39.5px;
    font-size: 22px;
    font-weight: 400;
  }
  .contacts__icon {
    width: 22px;
    height: 22px;
    margin-right: 18px;
    fill: var(--accent);
    flex: none;
  }
</style>
</head>
<body>
  <section class="card card--front" aria-label="Business card front">
    <div class="wordmark"><span class="wordmark__square"></span>DLQ MARROWFIELD</div>

    <div class="holder">
      <h1 class="holder__name">Derya Koltan</h1>
      <span class="holder__rule"></span>
    </div>

    <ul class="contacts">
      <li class="contacts__item">
        <svg class="contacts__icon" viewBox="0 0 24 24" aria-hidden="true"><path d="M6.6 10.8c1.4 2.8 3.8 5.1 6.6 6.6l2.2-2.2c.3-.3.7-.4 1-.2 1.1.4 2.3.6 3.6.6.6 0 1 .4 1 1V20c0 .6-.4 1-1 1C10.6 21 3 13.4 3 4c0-.6.4-1 1-1h3.5c.6 0 1 .4 1 1 0 1.3.2 2.5.6 3.6.1.3 0 .7-.2 1L6.6 10.8z"/></svg>
        0400 555 173
      </li>
      <li class="contacts__item">
        <svg class="contacts__icon" viewBox="0 0 24 24" aria-hidden="true"><path d="M2 5h20v14H2z"/><path d="M2.5 5.5 12 12.5l9.5-7" fill="none" stroke="#000" stroke-width="1.6"/></svg>
        info@dlqmarrowfield.com.au
      </li>
      <li class="contacts__item">
        <svg class="contacts__icon" viewBox="0 0 24 24" aria-hidden="true"><circle cx="12" cy="12" r="10"/><g fill="none" stroke="#000" stroke-width="1.3"><ellipse cx="12" cy="12" rx="4.5" ry="10"/><path d="M2 12h20M4 7h16M4 17h16"/></g></svg>
        www.dlqmarrowfield.com.au
      </li>
    </ul>
  </section>

  <section class="card card--back" aria-label="Business card back">
    <div class="wordmark"><span class="wordmark__square"></span>DLQ MARROWFIELD</div>
  </section>
</body>
</html>
```